Maplebrook Self Storage - Business Sign

The sign we are needing designed is our main road sign for our self-storage business. The dimensions of the sign are 57 inches tall x 96 inches wide. We require that our attached logo be on the sign as well as our phone number: 478-216-7745 and website www.MaplebrookStorage.net. Optional information that can be added but not required is our address: 418 Delmont Ridge Pkwy, Hollis Springs, GA 31044.

Industry/Entity Type

Self Storage

Font styles to use
Sans Serif

```html
<!DOCTYPE html>
<html lang="en">
<head>
<meta charset="utf-8">
<title>Maplebrook Self Storage – Road Sign</title>
<link rel="stylesheet" href="https://fonts.googleapis.com/css2?family=Barlow:wght@500&family=Barlow+Condensed:wght@400;500;700&display=swap">
<style>
  :root {
    --backdrop: #e6e6e6;
    --sign-white: #f7f7f7;
    --charcoal: #444546;
    --brand-blue: #2b7fc9;
    --stripe-blue: #5ba0dd;
    --white: #ffffff;
  }
  html, body {
    margin: 0;
    width: 1200px;
    height: 794px;
    overflow: hidden;
    background: var(--backdrop);
  }
  .sign {
    position: absolute;
    left: 0;
    top: 42px;
    width: 1200px;
    height: 710px;
    background: var(--sign-white);
    display: flex;
    flex-direction: column;
  }
  .brand-panel {
    height: 528px;
    display: flex;
    flex-direction: column;
    align-items: center;
    justify-content: center;
    color: var(--charcoal);
    font-family: "Barlow", sans-serif;
    font-weight: 500;
  }
  .brand-name {
    font-size: 178px;
    line-height: 1;
    letter-spacing: 2px;
    text-transform: uppercase;
  }
  .brand-tagline {
    margin-top: 36px;
    font-size: 92px;
    line-height: 1;
    letter-spacing: 27px;
    margin-right: -27px;
    text-transform: uppercase;
  }
  .call-band {
    height: 89px;
    background: var(--brand-blue);
    position: relative;
    display: flex;
    align-items: center;
    justify-content: center;
    gap: 16px;
    color: var(--white);
    font-family: "Barlow Condensed", sans-serif;
  }
  .call-band .stripes {
    position: absolute;
    top: 25px;
    width: 184px;
    height: 38px;
    background:
      linear-gradient(var(--stripe-blue), var(--stripe-blue)) 0 0 / 100% 5px no-repeat,
      linear-gradient(var(--stripe-blue), var(--stripe-blue)) 0 16px / 100% 5px no-repeat,
      linear-gradient(var(--stripe-blue), var(--stripe-blue)) 0 33px / 100% 5px no-repeat;
  }
  .stripes.left { left: 0; }
  .stripes.right { right: 0; }
  .phone-icon { width: 58px; height: 58px; }
  .call-text { font-size: 70px; line-height: 1; font-weight: 400; letter-spacing: 1px; }
  .call-text strong { font-weight: 700; margin-left: 8px; }
  .info-band {
    flex: 1;
    background: var(--charcoal);
    display: flex;
    align-items: center;
    justify-content: center;
    color: var(--white);
    font-family: "Barlow Condensed", sans-serif;
    font-weight: 500;
    font-size: 33px;
  }
  .info-item { display: flex; align-items: center; gap: 10px; white-space: nowrap; }
  .info-item svg { width: 22px; height: 22px; }
  .website b { font-weight: 700; }
  .divider {
    width: 2px;
    height: 52px;
    margin: 0 32px;
    background: #5b5c5d;
  }
</style>
</head>
<body>
  <main class="sign">
    <section class="brand-panel">
      <div class="brand-name">Maplebrook</div>
      <div class="brand-tagline">Self Storage</div>
    </section>

    <section class="call-band">
      <span class="stripes left"></span>
      <svg class="phone-icon" viewBox="0 0 58 58" aria-hidden="true">
        <circle cx="29" cy="29" r="29" fill="#3a3b3c"/>
        <path d="M20 16c2-1 4 0 5 2l2 5c1 2 0 3-1 4l-2 2c1 3 4 6 7 7l2-2c1-1 2-2 4-1l5 2c2 1 3 3 2 5-1 3-4 5-7 5-11-1-20-10-21-21 0-3 2-6 4-8z" fill="#fff"/>
        <path d="M32 15a12 12 0 0 1 11 11M32 21a6 6 0 0 1 5 5" stroke="#fff" stroke-width="2.6" fill="none" stroke-linecap="round"/>
      </svg>
      <span class="call-text">CALL US <strong>478-216-7745</strong></span>
      <span class="stripes right"></span>
    </section>

    <footer class="info-band">
      <span class="info-item website">
        <svg viewBox="0 0 22 22" aria-hidden="true">
          <circle cx="11" cy="11" r="10" fill="#4a97dc"/>
          <g stroke="#fff" stroke-width="1.4" fill="none">
            <circle cx="11" cy="11" r="6.5"/>
            <ellipse cx="11" cy="11" rx="3" ry="6.5"/>
            <path d="M4.5 11h13"/>
          </g>
        </svg>
        <span>www.<b>MaplebrookStorage</b>.net</span>
      </span>
      <span class="divider"></span>
      <span class="info-item address">
        <svg viewBox="0 0 22 22" aria-hidden="true">
          <path d="M11 1a7.5 7.5 0 0 1 7.5 7.5C18.5 14 11 21 11 21S3.5 14 3.5 8.5A7.5 7.5 0 0 1 11 1z" fill="#4a97dc"/>
          <circle cx="11" cy="8.5" r="3" fill="#fff"/>
        </svg>
        <span>418 Delmont Ridge Pkwy, Hollis Springs, GA 31044.</span>
      </span>
    </footer>
  </main>
</body>
</html>
```